Private Security Company Business Card and Logo Design

Looking for a modern conservative business card design for our new private security company Halvern Guard Partners, Inc. or HGP for short.
Private Security Services. The current logo we have is not very good and honestly would like a sharp logo for the card instead of using the one we have now. Open to ideas. I am easy just looking for something nicer then what I can personally design on cardloomix. I searched on zintrova for Security Company business cards went to images and found some nice designs that were made here.

Target Market(s)

Security Services

Industry/Entity Type

Business

Contact Information for Business Card

Halvern Guard Partners, Inc.
President, cell,office,fax,email, website,
Logo etc, whatever is needed for a standard business card
Can provide personal Information later.

Colors
0556a4
ffffff
474747

Requirements
Must have
• Modern but conservative,
Nice to have
• color choices
• Blue, white, Grey

```html
<!DOCTYPE html>
<html lang="en">
<head>
<meta charset="utf-8">
<title>Halvern Guard Partners – Business Card</title>
<link href="https://fonts.googleapis.com/css2?family=Open+Sans:wght@400;600;700&display=swap" rel="stylesheet">
<style>
  :root {
    --brand-blue: #0556a4;
    --brand-blue-light: #2f86d0;
    --ink-grey: #474747;
    --rule-grey: #5a5a5a;
    --card-white: #ffffff;
    --card-shade: #eeeeee;
    --canvas-bg: #d9d6d1;
  }
  * { box-sizing: border-box; margin: 0; padding: 0; }
  html, body {
    width: 1200px; height: 1023px; overflow: hidden;
    background: var(--canvas-bg);
    font-family: "Open Sans", Arial, sans-serif;
  }
  .card {
    position: absolute;
    width: 560px; height: 320px;
    background: linear-gradient(135deg, var(--card-white) 40%, var(--card-shade));
    box-shadow: 0 10px 26px rgba(0,0,0,.22);
    overflow: hidden;
  }
  .card--front { left: 70px; top: 110px; }
  .card--back { left: 570px; top: 590px; }

  .corner-band {
    position: absolute; width: 170px; height: 70px;
    background: linear-gradient(180deg, var(--brand-blue-light), var(--brand-blue));
    border: 5px solid #8a8a8a;
  }
  .corner-band--top { top: -5px; right: -5px; border-radius: 0 0 0 60px; }
  .corner-band--bottom { bottom: -5px; left: -5px; border-radius: 0 60px 0 0; }

  .brand-mark {
    display: flex; align-items: center; gap: 10px;
    color: var(--brand-blue); font-weight: 700;
  }
  .brand-mark__dot {
    width: 14px; height: 14px; border-radius: 50%;
    background: var(--brand-blue);
  }
  .front__logo {
    position: absolute; left: 0; right: 0; top: 96px;
    justify-content: center; font-size: 48px; letter-spacing: 2px;
  }
  .front__company {
    position: absolute; left: 0; right: 0; top: 170px;
    text-align: center; color: var(--brand-blue);
    font-size: 19px; font-weight: 600;
  }
  .front__web {
    position: absolute; left: 0; right: 0; top: 214px;
    text-align: center; color: var(--ink-grey);
    font-size: 16px; letter-spacing: 3px;
  }

  .back__contacts {
    position: absolute; left: 44px; top: 40px;
    display: grid; grid-template-columns: 200px 240px; row-gap: 10px;
    color: var(--brand-blue); font-size: 15px;
  }
  .contact { display: flex; align-items: center; gap: 8px; }
  .contact svg { width: 13px; height: 13px; fill: var(--ink-grey); flex: none; }

  .back__name-rule {
    position: absolute; left: 0; right: 0; top: 140px;
    display: flex; align-items: center; gap: 14px;
  }
  .back__name-rule .rule { flex: 1; height: 1px; background: var(--rule-grey); }
  .name { color: var(--brand-blue); font-size: 26px; font-weight: 600; }
  .name .title { color: var(--ink-grey); font-size: 13px; font-weight: 400; }

  .back__address {
    position: absolute; left: 44px; top: 220px;
    color: var(--brand-blue); font-size: 15px; line-height: 1.4;
    display: flex; gap: 8px;
  }
  .back__address svg { width: 12px; height: 14px; margin-top: 4px; fill: var(--ink-grey); }
  .back__brand {
    position: absolute; right: 40px; top: 200px; text-align: center;
  }
  .back__brand .brand-mark { font-size: 32px; justify-content: center; }
  .back__brand-name {
    margin-top: 6px; color: var(--brand-blue); font-size: 13px; font-weight: 600;
  }
</style>
</head>
<body>
  <section class="card card--front">
    <div class="corner-band corner-band--top"></div>
    <div class="corner-band corner-band--bottom"></div>
    <div class="brand-mark front__logo"><span class="brand-mark__dot"></span>HGP</div>
    <p class="front__company">Halvern Guard Partners</p>
    <p class="front__web">www.halvernguard.com</p>
  </section>

  <section class="card card--back">
    <div class="back__contacts">
      <span class="contact"><svg viewBox="0 0 10 14"><rect x="1" y="0" width="8" height="14" rx="1.5"/></svg>55-210-48736</span>
      <span class="contact"><svg viewBox="0 0 14 14"><rect x="0" y="4" width="14" height="10" rx="1"/><rect x="3" y="0" width="8" height="5"/></svg>55-210-48712</span>
      <span class="contact"><svg viewBox="0 0 14 14"><path d="M3 0h3l1 4-2 1a8 8 0 0 0 4 4l1-2 4 1v3c0 1-1 2-2 2C6 13 1 8 1 2c0-1 1-2 2-2z"/></svg>55-210-48790</span>
      <span class="contact"><svg viewBox="0 0 14 10"><path d="M0 0h14v10H0z M1 1l6 5 6-5" /></svg>info@halvernguard.com</span>
    </div>
    <div class="back__name-rule">
      <span class="rule"></span>
      <p class="name">Your Name,<span class="title"> President</span></p>
      <span class="rule"></span>
    </div>
    <div class="back__address">
      <svg viewBox="0 0 12 14"><path d="M6 0a5 5 0 0 1 5 5c0 4-5 9-5 9S1 9 1 5a5 5 0 0 1 5-5z"/></svg>
      <p>Your Addressin<br>in just two line</p>
    </div>
    <div class="back__brand">
      <div class="brand-mark"><span class="brand-mark__dot"></span>HGP</div>
      <p class="back__brand-name">Halvern Guard Partners, Inc.</p>
    </div>
  </section>
</body>
</html>
```